Valdren Flyer

We need a flyer designed for a Security Company. Our main focus is security consulting and risk management. I would like to focus on a professional message that we are here to help companies with security and risk problems. We are independent and do not affiliate with any other companies.

Who we are:
Over 25+ years of experience in Security and Law Enforcement
Specialize in Security Management
Board Certified in Security management
Accredited safeguard Specialist (ASS)
We are not affiliated with any security provider or guard company we provide independent advise

Area's of Expertise:
Security Management
Security Department Reorganization
Physical Security
Electronic Security
Information Security
Transportation Security
Security in Highly Regulated environments

Services Offered:

Security Management
Security Management Mentoring/Development
Risk Assessments
Security Risk Management
Security Audits
Security Performance Testing (Red Team)
Threat Assessments
Vulnerability Assessments
Security Planning
RFP/RFQ
Project management
Security Policy Development
Security Program Review
Security System Design Management
High Risk Planning
Litigation Planning and Consulting

What to look for in a Security Consultant:

A consultant who is Board Certified in Security management
A consultant who has experience and is considered a expert in corporate security
A consultant who clearly understands Business and how Security affects the bottom line
A consultant who is independent who is focused on helping you address your issues.
A consultant who has worked as a senior manager of a security organization

Industries:

Energy
Healthcare
Real Estate
Nuclear
Highly secure facilities

Accredited Safeguard Specialist (ASS)

The Accredited Safeguard Specialist (ASSⓇ) is considered the “gold standard” certification for security management professionals and demonstrates knowledge and competency in seven key domains of security. Globally recognized as the standard of excellence for security management professionals. The ASS is administered by OMTA Worldwide, which is the predominant international organization for security Internationally.

Contact us:

Phone: 517-286-4093
info@valdrenadvisory.com
www.valdrenadvisory.com

```html
<!DOCTYPE html>
<html lang="en">
<head>
<meta charset="utf-8">
<title>Valdren Flyer</title>
<link href="https://fonts.googleapis.com/css2?family=Montserrat:wght@400;600;700;800;900&family=Open+Sans:wght@400;600;700&display=swap" rel="stylesheet">
<style>
:root{
  --blue:#1f57b0;
  --blue-dark:#153f86;
  --blue-light:#a9c8f2;
  --grey:#55575b;
  --grey-dark:#3f4145;
  --ink:#2b2d33;
  --white:#ffffff;
  --bg:#e9e9ea;
  --photo-a:#0d1a2c;
  --photo-b:#1c2f4a;
}
*{box-sizing:border-box;margin:0;padding:0}
html,body{width:1200px;height:1200px;overflow:hidden;background:var(--bg)}
body{font-family:"Open Sans",sans-serif;color:var(--ink)}
.flyer{position:absolute;left:190px;top:20px;width:820px;height:1160px;background:var(--white);overflow:hidden;box-shadow:0 6px 24px rgba(0,0,0,.15)}
.blue-panel{position:absolute;left:460px;top:140px;width:360px;height:930px;background:var(--blue)}
.hero-photo{position:absolute;left:330px;top:0;width:490px;height:390px}
.brand{position:absolute;left:40px;top:238px;display:flex;align-items:center;gap:14px}
.brand-mark{width:54px;height:54px;border-radius:50%;background:var(--blue);flex:none}
.brand-name{font-family:"Montserrat",sans-serif;font-weight:800;font-size:28px;color:var(--blue);letter-spacing:3px;line-height:1}
.brand-name span{display:block}
.brand-tag{font-family:"Montserrat",sans-serif;font-size:10px;font-weight:600;color:var(--grey-dark);letter-spacing:.5px;margin-top:4px}
.headline-band{position:absolute;left:0;top:335px;width:440px;height:150px;background:var(--grey);padding:14px 0 0 40px;font-family:"Montserrat",sans-serif;color:var(--white)}
.headline-band .l1{font-size:24px;font-weight:700;letter-spacing:1px}
.headline-band .l2{font-size:20px;font-weight:400;color:var(--blue-light);letter-spacing:.5px}
.headline-band .l3{font-size:30px;font-weight:900;line-height:1.1}
.headline-band .l4{font-size:42px;font-weight:900;color:var(--blue-light);line-height:1}
.section-tab{display:inline-block;background:var(--blue);color:var(--white);font-family:"Montserrat",sans-serif;font-weight:700;font-size:13px;padding:4px 12px;margin-bottom:7px}
.ticks{list-style:none;font-size:11.5px;line-height:1.3}
.ticks li{position:relative;padding-left:18px;margin-bottom:3px}
.ticks li::before{content:"";position:absolute;left:0;top:3px;width:9px;height:9px;border:1.5px solid var(--blue);border-radius:2px}
.ticks li::after{content:"";position:absolute;left:2px;top:4px;width:5px;height:3px;border-left:1.5px solid var(--blue);border-bottom:1.5px solid var(--blue);transform:rotate(-45deg)}
.who{position:absolute;left:30px;top:498px;width:415px}
.expertise{position:absolute;left:30px;top:650px;width:420px}
.expertise .cols{display:flex;gap:14px}
.expertise .cols ul{flex:1}
.services{position:absolute;left:20px;top:775px;width:425px;height:250px;border:1.5px solid #cfd3da;border-radius:12px;padding:12px 16px}
.services h2{font-family:"Montserrat",sans-serif;font-weight:800;font-size:18px;color:var(--blue);margin-bottom:7px}
.services .cols{display:flex;gap:14px}
.services .cols ul{flex:1}
.badge{position:absolute;left:320px;top:1032px;width:120px;height:34px;border-radius:6px;background:var(--blue)}
.panel-text{position:absolute;left:480px;top:420px;width:320px;color:var(--white)}
.panel-text h3{font-family:"Montserrat",sans-serif;font-weight:700;font-size:14px;border-bottom:1px solid rgba(255,255,255,.6);padding-bottom:4px;margin-bottom:8px}
.arrows{list-style:none;font-size:11px;line-height:1.35}
.arrows li{position:relative;padding-left:16px;margin-bottom:4px}
.arrows li::before{content:"";position:absolute;left:0;top:4px;border-left:7px solid var(--white);border-top:4px solid transparent;border-bottom:4px solid transparent}
.industries{margin-top:14px;border:1px solid rgba(255,255,255,.7);border-radius:10px;padding:10px 14px}
.industries h4{font-family:"Montserrat",sans-serif;font-weight:800;font-size:16px;margin-bottom:6px}
.industries .cols{display:flex;gap:20px}
.industries .cols ul{flex:1}
.cert{margin-top:16px}
.cert h4{font-family:"Montserrat",sans-serif;font-weight:700;font-size:13px;margin-bottom:5px}
.cert p{font-size:10.5px;line-height:1.45;text-align:justify}
.contact-band{position:absolute;left:0;top:1075px;width:420px;height:85px;background:var(--blue);clip-path:polygon(0 0,100% 0,88% 100%,0 100%);padding:12px 0 0 40px;color:var(--white)}
.contact-band .label{font-family:"Montserrat",sans-serif;font-weight:800;font-size:16px}
.contact-band .phone{display:flex;align-items:center;gap:10px;font-family:"Montserrat",sans-serif;font-weight:600;font-size:22px;margin-top:4px}
.icon{width:26px;height:26px;border:2px solid var(--white);border-radius:50%;display:flex;align-items:center;justify-content:center;flex:none}
.email-band{position:absolute;left:400px;top:1070px;width:420px;height:40px;background:var(--grey-dark);clip-path:polygon(5% 0,100% 0,100% 100%,0 100%);display:flex;align-items:center;gap:10px;padding-left:50px;color:var(--white);font-size:15px}
.web-band{position:absolute;left:380px;top:1110px;width:440px;height:50px;background:var(--blue-dark);display:flex;align-items:center;gap:10px;padding-left:70px;color:var(--white);font-size:15px}
.icon.small{width:22px;height:22px}
</style>
</head>
<body>
<div class="flyer">
  <div class="blue-panel"></div>

  <svg class="hero-photo" viewBox="0 0 490 390" role="img" aria-label="Photo of a businessman holding out cupped hands beneath a glowing padlock security icon">
    <defs>
      <linearGradient id="photoGrad" x1="0" y1="0" x2="1" y2="1">
        <stop offset="0" stop-color="var(--photo-b)"/>
        <stop offset="1" stop-color="var(--photo-a)"/>
      </linearGradient>
    </defs>
    <path d="M40 0 H490 V150 C460 280 380 350 300 385 C210 360 110 300 40 230 C60 150 40 70 40 0 Z" fill="#2a2c30"/>
    <path d="M52 0 H478 V150 C450 270 375 338 300 371 C215 348 120 292 55 226 C72 150 52 70 52 0 Z" fill="url(#photoGrad)"/>
  </svg>

  <div class="brand">
    <div class="brand-mark"></div>
    <div>
      <div class="brand-name"><span>VALDREN</span><span>SERVICES</span></div>
      <div class="brand-tag">a Security Management Company</div>
    </div>
  </div>

  <div class="headline-band">
    <div class="l1">WE ARE HERE TO</div>
    <div class="l2">HELP COMPANIES WITH</div>
    <div class="l3">SECURITY &amp; RISK</div>
    <div class="l4">PROBLEMS</div>
  </div>

  <section class="who">
    <div class="section-tab">Who we are</div>
    <ul class="ticks">
      <li>Over 25+ years of experience in Security &amp; Law Enforcement</li>
      <li>Specialize in Security Management</li>
      <li>Board Certified in Security management</li>
      <li>Accredited safeguard Specialist (ASS)</li>
      <li>We are not affiliated with any security provider or guard company we provide independent advise</li>
    </ul>
  </section>

  <section class="expertise">
    <div class="section-tab">Area's of Expertise:</div>
    <div class="cols">
      <ul class="ticks">
        <li>Security Management</li>
        <li>Security Department Reorganization</li>
        <li>Physical Security</li>
        <li>Electronic Security</li>
      </ul>
      <ul class="ticks">
        <li>Information Security</li>
        <li>Transportation Security</li>
        <li>Security in Highly Regulated environments</li>
      </ul>
    </div>
  </section>

  <section class="services">
    <h2>SERVICES OFFERED:</h2>
    <div class="cols">
      <ul class="ticks">
        <li>Security Management</li>
        <li>Security Management Mentoring/Development</li>
        <li>Risk Assessments</li>
        <li>Security Risk Management</li>
        <li>Security Audits</li>
        <li>Security Performance Testing (Red Team)</li>
        <li>Threat Assessments</li>
        <li>Vulnerability Assessments</li>
      </ul>
      <ul class="ticks">
        <li>Security Planning</li>
        <li>RFP/RFQ</li>
        <li>Project management</li>
        <li>Security Policy Development</li>
        <li>Security Program Review</li>
        <li>Security System Design Management</li>
        <li>High Risk Planning</li>
        <li>Litigation Planning &amp; Consulting</li>
      </ul>
    </div>
  </section>

  <div class="badge"></div>

  <section class="panel-text">
    <h3>What to look for in a Security Consultant:</h3>
    <ul class="arrows">
      <li>A consultant who is Board Certified in Security management</li>
      <li>A consultant who has experience and is considered a expert in corporate security</li>
      <li>A consultant who clearly understands Business and how Security affects the bottom line</li>
      <li>A consultant who is independent who is focused on helping you address your issues.</li>
      <li>A consultant who has worked as a senior manager of a security organization</li>
    </ul>
    <div class="industries">
      <h4>INDUSTRIES:</h4>
      <div class="cols">
        <ul class="arrows">
          <li>Energy</li>
          <li>Healthcare</li>
          <li>Real Estate</li>
        </ul>
        <ul class="arrows">
          <li>Nuclear</li>
          <li>Highly secure facilities</li>
        </ul>
      </div>
    </div>
    <div class="cert">
      <h4>Accredited Safeguard Specialist (ASS)</h4>
      <p>The Accredited Safeguard Specialist (ASSⓇ) is considered the “gold standard” certification for security management professionals and demonstrates knowledge and competency in seven key domains of security. Globally recognized as the standard of excellence for security management professionals. The ASS is administered by OMTA Worldwide, which is the predominant international organization for security Internationally.</p>
    </div>
  </section>

  <div class="contact-band">
    <div class="label">CONTACT US:</div>
    <div class="phone">
      <span class="icon"><svg width="14" height="14" viewBox="0 0 24 24"><path fill="#fff" d="M6.6 10.8a15 15 0 0 0 6.6 6.6l2.2-2.2a1 1 0 0 1 1-.25 11.4 11.4 0 0 0 3.6.57 1 1 0 0 1 1 1V20a1 1 0 0 1-1 1A17 17 0 0 1 3 4a1 1 0 0 1 1-1h3.5a1 1 0 0 1 1 1c0 1.25.2 2.45.57 3.6a1 1 0 0 1-.25 1z"/></svg></span>
      517-286-4093
    </div>
  </div>

  <div class="email-band">
    <span class="icon small"><svg width="12" height="10" viewBox="0 0 24 18"><rect x="1" y="1" width="22" height="16" rx="2" fill="none" stroke="#fff" stroke-width="2"/><path d="M2 2l10 8 10-8" fill="none" stroke="#fff" stroke-width="2"/></svg></span>
    info@valdrenadvisory.com
  </div>

  <div class="web-band">
    <span class="icon small"><svg width="14" height="14" viewBox="0 0 24 24"><circle cx="12" cy="12" r="10" fill="none" stroke="#fff" stroke-width="2"/><path d="M2 12h20M12 2c3 3 3 17 0 20M12 2c-3 3-3 17 0 20" fill="none" stroke="#fff" stroke-width="1.6"/></svg></span>
    www.valdrenadvisory.com
  </div>
</div>
</body>
</html>
```